New website for Pilates Studio

I need a new version of my website
http://bellwetherstretch.biz/
I want an updated fresh look with an easier to read schedule that looks good on mobile phones as well as laptops.
Clean, simple, fresh and BOLD

Target Market(s)

All ages, genders and races

Coding

Coded - Design and coding required

Number of Pages Required

4 page

Colors
9bcb3c

Requirements
Must have
• Photos that mostly use the real images from our studio. Browse our facebook page, website or ask me for high quality images

```html
<!DOCTYPE html>
<html lang="en">
<head>
<meta charset="utf-8">
<title>Bellwether Stretch — Pilates &amp; Spiralflow Studio</title>
<link rel="stylesheet" href="https://fonts.googleapis.com/css2?family=Open+Sans:wght@300;400;600;700&family=Roboto:wght@400;500&display=swap">
<style>
  :root{
    --brand-green:#9bcb3c;
    --deep-green:#3d6b1f;
    --accent-yellow:#f4ef6a;
    --ink:#1f1f1f;
    --muted:#777;
    --footer-bg:#ececec;
    --hero-light:#fbe3a6;
    --hero-warm:#f6c96e;
  }
  *{margin:0;padding:0;box-sizing:border-box}
  html,body{width:1200px;height:1000px;overflow:hidden;background:#fff}
  body{position:relative;font-family:"Open Sans",sans-serif;color:var(--ink)}
  .top-rule{position:absolute;left:0;top:0;width:1200px;height:4px;background:var(--brand-green)}

  .site-header{position:absolute;left:0;top:4px;width:1200px;height:99px}
  .brand{position:absolute;left:234px;top:24px;display:flex;align-items:center;gap:10px}
  .brand-mark{width:42px;height:42px;border-radius:50%;background:#c9a227}
  .brand-name{font-family:"Open Sans",sans-serif;font-weight:700;font-size:24px;color:var(--deep-green);letter-spacing:-.3px}
  .main-nav{position:absolute;left:508px;top:41px;display:flex;font-family:"Roboto",sans-serif;font-size:15px}
  .main-nav a{color:var(--ink);text-decoration:none;padding:3px 11px 3px 0;margin-right:2px;line-height:19px}
  .main-nav a.is-active{background:var(--brand-green);padding:3px 12px;margin-right:11px}
  .phone{position:absolute;left:832px;top:40px;display:flex;align-items:center;gap:6px;font-family:"Roboto",sans-serif;font-weight:500;font-size:19px}

  .hero{position:absolute;left:0;top:103px;width:1200px;height:348px;
    background:linear-gradient(90deg,var(--hero-warm) 0%,var(--hero-light) 25%,#fff3cf 50%,var(--hero-light) 75%,var(--hero-warm) 100%)}

  .intro{position:absolute;left:0;top:451px;width:1200px;height:203px}
  .portrait{position:absolute;left:238px;top:44px;width:116px;height:117px;border-radius:50%;background:linear-gradient(160deg,#d9d9d9,#8a8a8a)}
  .intro-text{position:absolute;left:372px;top:50px;width:490px;font-size:15px;line-height:26.5px;color:var(--muted);font-weight:400}
  .intro-text strong{color:var(--ink);font-weight:400}
  .social{position:absolute;left:915px;top:49px;display:flex;gap:10px}
  .social span{width:21px;height:21px;border-radius:3px}
  .social .sq-blue{background:#3b5a9a}
  .social .sq-red{background:#c0392b}

  .feature-band{position:absolute;left:0;top:654px;width:1200px;height:185px;background:var(--brand-green);color:#fff}
  .feature{position:absolute}
  .feature h2{font-size:18px;font-weight:700;color:var(--accent-yellow);letter-spacing:.2px;margin-bottom:9px}
  .feature p{font-size:12px;line-height:19.5px;font-weight:600}
  .feature-mission{left:235px;top:33px;width:360px}
  .feature-classes{left:797px;top:33px;width:170px}
  .studio-photo{position:absolute;left:611px;top:0;width:172px;height:185px;background:linear-gradient(135deg,#e2b84a,#8a5a2a 60%,#3a2f2a)}
  .btn-outline{display:inline-block;margin-top:13px;border:2px solid #fff;padding:2px 8px;font-size:10.5px;font-weight:700;color:#fff;text-decoration:none;letter-spacing:.2px}

  .green-cert{position:absolute;left:0;top:839px;width:1200px;height:124px}
  .green-cert h3{position:absolute;left:235px;top:53px;font-size:15px;font-weight:700;color:var(--brand-green)}
  .cert-badge{position:absolute;left:428px;top:25px;width:82px;height:80px;border-radius:50%;background:linear-gradient(180deg,#2e8b57,#2c6fa3)}
  .green-cert p{position:absolute;left:523px;top:34px;width:445px;font-size:12px;line-height:19.5px;color:#555}

  .site-footer{position:absolute;left:0;top:963px;width:1200px;height:37px;background:var(--footer-bg);font-size:10px;color:var(--brand-green)}
  .footer-nav{position:absolute;left:236px;top:13px}
  .footer-nav a{color:var(--brand-green);text-decoration:none}
  .copyright{position:absolute;right:235px;top:13px}
</style>
</head>
<body>
  <div class="top-rule"></div>

  <header class="site-header">
    <div class="brand">
      <span class="brand-mark"></span>
      <span class="brand-name">Bellwether Stretch</span>
    </div>
    <nav class="main-nav">
      <a class="is-active" href="#">Home</a>
      <a href="#">Schedule</a>
      <a href="#">Instructors</a>
      <a href="#">Rates</a>
    </nav>
    <div class="phone">
      <svg width="15" height="15" viewBox="0 0 24 24" aria-hidden="true"><path fill="#1f1f1f" d="M6.6 10.8a15.1 15.1 0 0 0 6.6 6.6l2.2-2.2a1 1 0 0 1 1-.25 11.4 11.4 0 0 0 3.6.57 1 1 0 0 1 1 1V20a1 1 0 0 1-1 1A17 17 0 0 1 3 4a1 1 0 0 1 1-1h3.5a1 1 0 0 1 1 1c0 1.25.2 2.45.57 3.57a1 1 0 0 1-.25 1z"/></svg>
      <span>555 014 2368</span>
    </div>
  </header>

  <section class="hero" role="img" aria-label="Photo of a dancer in a pike handstand on a Pilates chair in front of sunlit curtains"></section>

  <section class="intro">
    <div class="portrait" role="img" aria-label="Black and white portrait of a studio instructor"></div>
    <p class="intro-text"><strong>Bellwether Stretch</strong> Pilates and SPIRALFLOW Studio, in the heart of Cedar Hollow Village, is a warm, inviting studio where students and teachers alike are supported and encouraged to discover and grow at an individual pace through the field of integrated movement.</p>
    <div class="social"><span class="sq-blue"></span><span class="sq-red"></span></div>
  </section>

  <section class="feature-band">
    <div class="feature feature-mission">
      <h2>WHY WE’RE SPECIAL</h2>
      <p>Our mission is to promote long-term emotional and physical health through joyful, integrated movement training and to inspire and nurture our clients to learn more deeply about themselves and connect with fellow students and the community.</p>
    </div>
    <div class="studio-photo" role="img" aria-label="Photo of a student working on a reformer in the sunny studio"></div>
    <div class="feature feature-classes">
      <h2>CLASSES</h2>
      <p>We offer one-on-one sessions, group reformer classes and mat classes.</p>
      <a class="btn-outline" href="#">CHECK SCHEDULE</a>
    </div>
  </section>

  <section class="green-cert">
    <h3>WE’RE GREEN CERTIFIED!</h3>
    <div class="cert-badge" role="img" aria-label="Green business certification badge"></div>
    <p>Join our community in creating a sustainable future. We enjoy the benefits of protecting our environment with daily practice: &nbsp; recycling, using efficient lighting, conserving water use &amp; acting responsibly.</p>
  </section>

  <footer class="site-footer">
    <nav class="footer-nav"><a href="#">Home</a> / <a href="#">Schedule</a> / <a href="#">Instructors</a> / <a href="#">Rates</a></nav>
    <span class="copyright">2015, Bellwether Stretch</span>
  </footer>
</body>
</html>
```